Dental office needs flyer Design

We need a flier design for our Dental office based in Rockville MD. We provide premium dental care services including General and Ortho.

Flier Audience - Upper Middle Class, Individual professionals, Family, urban living,

Flier Focus - Promote "Grin Circle" program offered by the office
Key Highlights of the program - $69 for individual, $59 per person for family of two, $49 per person for a family 3, $39 per person for a family of 4. Design thoughts - Circle from big size to small with visual representation of individual and family size. The subscription is per month and annual membership, Also with the membership member will receive 15 - 25% of procedures. 3 - 4 cleanings a year, One XRay per year, One Emergency Exam per year, easy monthly payments, No Deductible, No yearly maximums, No Exclusions.

Flier Design considerations
Door Hanger, Eye Catchy shape,

Dental Office Highlights - No more than 9 patients a day so no double booking, no waiting; Before and after hours appointments, weekend appointments are available for emergencies, Direct access to Dentist,

Services Provided
1. Preventative Care
2. Orthodontics - Braces, Clearomet,
3. Cosmetic - Veneers, Teeth Whitening, Bonding
4. Bridges, Implants, Crown, Filling,
5. Dentures
6. Root Canal, Extractions, Gum Treatments

Location - 2836 Thornbury Ln Rockville MD 20853
PH: 301 555 0148
Website : www.DentistKalvo.com

Target Market(s)

Upper Middle Class, Individual professionals, Family, urban living,

Industry/Entity Type

Dental

Font styles to use
Decorative
Script

Requirements
Must have
• Promote "Grin Circle" program offered by the office
• Key Highlights of the program - $69 for individual, $59 per person for family of two, $49 per person for a family 3, $39 per person for a family of 4. Design thoughts - Circle from big size to small with visual representation of individual and family size. The subscription is per month and annual membership, Also with the membership member will receive 15 - 25% of procedures. 3 - 4 cleanings a year, One XRay per year, One Emergency Exam per year, easy monthly payments, No Deductible, No yearly maximums, No Exclusions.
• Location - 2836 Thornbury Ln Rockville MD 20853
• PH: 301 555 0148
• Website : www.DentistKalvo.com
Nice to have
• Eye Catchy Shape for Flier

```html
<!DOCTYPE html>
<html lang="en">
<head>
<meta charset="utf-8">
<title>Grin Circle Door Hanger</title>
<link rel="stylesheet" href="https://fonts.googleapis.com/css2?family=Fredoka:wght@600;700&family=Oswald:wght@500;600&family=Signika:wght@400;600;700&family=PT+Sans:wght@400;700&display=swap">
<style>
:root{
  --page:#ecebe8;
  --hole:#ecebe8;
  --green-dark:#2f7a32;
  --green-mid:#3f9a3a;
  --green-light:#8cc63f;
  --lime:#c4d52c;
  --white:#ffffff;
  --text-green:#2f7a32;
}
*{margin:0;padding:0;box-sizing:border-box}
html,body{width:1175px;height:1200px;overflow:hidden;background:var(--page)}
.canvas{position:relative;width:1175px;height:1200px}
.hanger{position:absolute;top:50px;width:425px;height:1100px;background:var(--white);overflow:hidden;box-shadow:4px 6px 14px rgba(0,0,0,.25)}
.hanger--front{left:132px}
.hanger--back{left:617px}
.layer{position:absolute;left:0;top:0;width:425px;height:1100px}
.hole{position:absolute;left:150px;top:62px;width:124px;height:124px;border-radius:50%;background:var(--hole);border:3px solid var(--white);z-index:5}
.slit{position:absolute;left:0;top:0;z-index:4}
.brand{position:absolute;left:262px;top:34px;width:150px;text-align:center;font-family:"Signika",sans-serif;color:var(--text-green)}
.brand__mark{width:44px;height:44px;border-radius:50%;background:var(--text-green);margin:0 auto 6px}
.brand__name{font-weight:700;font-size:17px;letter-spacing:.5px}
.brand__tagline{font-family:"Signika",sans-serif;font-weight:700;font-size:10.5px;color:#222;line-height:13px;margin-top:4px}
.title{position:absolute;right:12px;top:178px;text-align:right;font-family:"Fredoka",sans-serif;font-weight:700;font-size:44px;line-height:50px;color:var(--lime);text-shadow:1px 2px 0 var(--green-dark);letter-spacing:1px}
.photo-circle{position:absolute;width:140px;height:140px;border-radius:50%;border:4px solid var(--white);box-shadow:0 8px 8px -4px rgba(0,0,0,.35)}
.price{position:absolute;width:90px;height:90px;border-radius:50%;background:var(--white);display:flex;align-items:center;justify-content:center;font-family:"Oswald",sans-serif;font-weight:600;font-size:46px;color:var(--text-green);letter-spacing:-1px}
.price sup{font-size:20px;margin-top:-18px;margin-right:1px}
.price::after{content:"";position:absolute;top:4px;width:0;height:0;border:12px solid transparent}
.price--left::after{left:-8px;border-right-color:var(--white);transform:rotate(35deg)}
.price--right::after{right:-8px;border-left-color:var(--white);transform:rotate(-35deg)}
.plan{position:absolute;font-family:"Signika",sans-serif;font-weight:600;font-size:16px;line-height:20px;color:var(--white);text-transform:uppercase}
.terms{position:absolute;left:18px;top:950px;width:390px;text-align:center;font-family:"Signika",sans-serif;font-weight:700;font-size:12.4px;line-height:17px;color:var(--white)}
.site{position:absolute;left:0;width:425px;text-align:center;font-family:"Signika",sans-serif;font-weight:700;color:var(--white);text-shadow:1px 1px 2px rgba(0,0,0,.3)}
.site--front{top:1050px;font-size:21px}
.doctor{position:absolute;left:246px;top:259px;width:164px;height:164px;border-radius:50%;border:5px solid var(--white);overflow:hidden;z-index:3}
.doctor__name{position:absolute;left:0;bottom:14px;width:100%;text-align:center;font-family:"PT Sans",sans-serif;font-size:11px;color:#111}
.highlights{position:absolute;left:0;top:428px;width:425px;text-align:center;font-family:"PT Sans",sans-serif;font-size:19px;line-height:23.5px;color:var(--white)}
.services-title{position:absolute;left:23px;top:583px;width:378px;height:44px;background:var(--white);border-radius:4px;display:flex;align-items:center;justify-content:center;font-family:"Signika",sans-serif;font-weight:700;font-size:27px;letter-spacing:1.5px;color:var(--text-green);box-shadow:0 6px 6px -3px rgba(0,0,0,.3)}
.services{position:absolute;left:14px;top:645px;list-style:none;font-family:"Signika",sans-serif;font-size:19px;color:var(--white)}
.services li{display:flex;align-items:center;height:29.3px}
.services svg{margin-right:11px;flex:none}
.map{position:absolute;left:22px;top:808px;width:379px;height:170px;border-radius:8px;border:3px solid var(--white);background:linear-gradient(135deg,#efe9d6,#f3e7b0 55%,#dfe6cf)}
.contact{position:absolute;left:0;width:425px;text-align:center;font-family:"Signika",sans-serif;font-weight:700;color:var(--white);text-shadow:1px 1px 2px rgba(0,0,0,.3)}
.contact--phone{top:990px;font-size:22px;display:flex;justify-content:center;align-items:center;gap:8px}
.contact--web{top:1022px;font-size:22px}
.contact--address{top:1052px;font-size:19px}
</style>
</head>
<body>
<div class="canvas">

  <!-- Front side: membership plans -->
  <section class="hanger hanger--front">
    <svg class="layer" viewBox="0 0 425 1100" aria-hidden="true">
      <defs>
        <linearGradient id="frontGreen" x1="0" y1="0" x2="1" y2="0">
          <stop offset="0" stop-color="#3a923a"/>
          <stop offset="1" stop-color="#8cc63f"/>
        </linearGradient>
        <linearGradient id="frontBottom" x1="0" y1="0" x2="1" y2="0">
          <stop offset="0" stop-color="#8cc63f"/>
          <stop offset="1" stop-color="#7fbf3c"/>
        </linearGradient>
      </defs>
      <path d="M0 382 Q260 392 425 262 L425 1100 L0 1100 Z" fill="var(--green-dark)"/>
      <path d="M0 405 Q270 408 425 290 L425 1100 L0 1100 Z" fill="url(#frontGreen)"/>
      <path d="M0 1040 Q220 1030 425 1010 L425 1100 L0 1100 Z" fill="url(#frontBottom)"/>
    </svg>
    <svg class="layer" viewBox="0 0 425 1100" role="img" aria-label="Photo of a smiling woman with white teeth">
      <path d="M0 0 L230 0 Q275 60 265 190 Q260 300 280 378 Q140 388 0 382 Z" fill="#e6c2ac"/>
    </svg>
    <svg class="slit" width="425" height="200" aria-hidden="true"><line x1="105" y1="0" x2="175" y2="80" stroke="#555" stroke-width="1.5"/></svg>
    <div class="hole"></div>

    <div class="brand">
      <div class="brand__mark"></div>
      <div class="brand__name">KALVO DENTAL</div>
      <div class="brand__tagline">EXCELLENCE IN CARE,<br>SKILL AND JUDGEMENT</div>
    </div>
    <h1 class="title">GRIN<br>CIRCLE</h1>

    <div class="photo-circle" role="img" aria-label="Photo of a smiling man with glasses" style="left:12px;top:411px;background:radial-gradient(circle at 50% 40%,#e8c9b0,#c9d6de)"></div>
    <div class="price price--left" style="left:173px;top:428px"><sup>$</sup>69</div>
    <div class="plan" style="left:286px;top:447px">For<br>Individual</div>

    <div class="plan" style="left:36px;top:582px">Per person<br>for family<br>of two</div>
    <div class="price price--right" style="left:165px;top:553px"><sup>$</sup>59</div>
    <div class="photo-circle" role="img" aria-label="Photo of a smiling couple" style="left:273px;top:530px;background:radial-gradient(circle at 50% 45%,#e3b898,#8a5a3c)"></div>

    <div class="photo-circle" role="img" aria-label="Photo of a family of three" style="left:12px;top:665px;background:radial-gradient(circle at 50% 45%,#eed2bd,#b98c6e)"></div>
    <div class="price price--left" style="left:173px;top:693px"><sup>$</sup>49</div>
    <div class="plan" style="left:286px;top:709px">Per person<br>for a family<br>of three</div>

    <div class="plan" style="left:36px;top:851px">Per person<br>a family of<br>four</div>
    <div class="price price--right" style="left:165px;top:826px"><sup>$</sup>39</div>
    <div class="photo-circle" role="img" aria-label="Photo of a family of four" style="left:273px;top:797px;background:radial-gradient(circle at 50% 45%,#f0d5c0,#a8c4d8)"></div>

    <p class="terms">The subscription is per month and annual membership, Also with the membership member will receive 15 - 25% of procedures. 3 - 4 cleanings a year, One XRay per year, One Emergency Exam per year, easy monthly payments, No Deductible, No yearly maximums, No Exclusions.</p>
    <div class="site site--front">WWW.DENTISTKALVO.COM</div>
  </section>

  <!-- Back side: office details -->
  <section class="hanger hanger--back">
    <svg class="layer" viewBox="0 0 425 1100" aria-hidden="true">
      <defs>
        <linearGradient id="backGreen" x1="0" y1="0" x2="1" y2="0">
          <stop offset="0" stop-color="#3a923a"/>
          <stop offset="1" stop-color="#8cc63f"/>
        </linearGradient>
      </defs>
      <rect width="425" height="1100" fill="url(#backGreen)"/>
      <path d="M0 960 Q220 990 425 1000 L425 1100 L0 1100 Z" fill="var(--green-dark)" opacity=".55"/>
      <path d="M0 1000 Q200 1010 425 990 L425 1100 L0 1100 Z" fill="#6fb23b"/>
    </svg>
    <svg class="layer" viewBox="0 0 425 1100" role="img" aria-label="Photo of a dental treatment room with patient chair">
      <path d="M0 0 L425 0 L425 265 Q260 395 0 382 Z" fill="var(--green-dark)"/>
      <path d="M0 0 L425 0 L425 250 Q260 380 0 365 Z" fill="#cfc8c0"/>
    </svg>
    <svg class="slit" width="425" height="200" aria-hidden="true"><line x1="102" y1="0" x2="172" y2="80" stroke="#555" stroke-width="1.5"/></svg>
    <div class="hole"></div>

    <div class="doctor" role="img" aria-label="Portrait photo of the dentist" style="background:radial-gradient(circle at 50% 40%,#b98a6c,#e9eef2 70%)">
      <span class="doctor__name">Dr Kalvo R.</span>
    </div>

    <p class="highlights">No more than 9 patients a day<br>so no double booking, no waiting<br>Before and after hours appointments<br>Weekend appointments are available<br>for emergencies<br>Direct access to Dentist</p>

    <h2 class="services-title">SERVICES PROVIDED</h2>
    <ul class="services">
      <li><svg width="14" height="14" viewBox="0 0 14 14"><circle cx="7" cy="7" r="7" fill="#fff"/><path d="M5.5 4 L8.5 7 L5.5 10" stroke="var(--green-dark)" stroke-width="2" fill="none"/></svg>Preventative Care</li>
      <li><svg width="14" height="14" viewBox="0 0 14 14"><circle cx="7" cy="7" r="7" fill="#fff"/><path d="M5.5 4 L8.5 7 L5.5 10" stroke="var(--green-dark)" stroke-width="2" fill="none"/></svg>Orthodontics - Braces, Clearomet,</li>
      <li><svg width="14" height="14" viewBox="0 0 14 14"><circle cx="7" cy="7" r="7" fill="#fff"/><path d="M5.5 4 L8.5 7 L5.5 10" stroke="var(--green-dark)" stroke-width="2" fill="none"/></svg>Cosmetic - Veneers, Teeth Whitening, Bonding</li>
      <li><svg width="14" height="14" viewBox="0 0 14 14"><circle cx="7" cy="7" r="7" fill="#fff"/><path d="M5.5 4 L8.5 7 L5.5 10" stroke="var(--green-dark)" stroke-width="2" fill="none"/></svg>Bridges, Implants, Crown, Filling,Dentures</li>
      <li><svg width="14" height="14" viewBox="0 0 14 14"><circle cx="7" cy="7" r="7" fill="#fff"/><path d="M5.5 4 L8.5 7 L5.5 10" stroke="var(--green-dark)" stroke-width="2" fill="none"/></svg>Root Canal, Extractions, Gum Treatments</li>
    </ul>

    <div class="map" role="img" aria-label="Street map of the Rockville area showing the office location"></div>

    <div class="contact contact--phone">
      <svg width="20" height="20" viewBox="0 0 20 20" aria-hidden="true"><rect width="20" height="20" rx="3" fill="#fff"/><path d="M6 4 L8 4 L9 7 L7.5 8.2 Q9 11.5 11.8 12.5 L13 11 L16 12 L16 14 Q15.5 16 13.5 16 Q5 15 4 6.5 Q4 4.5 6 4 Z" fill="var(--green-dark)"/></svg>
      301 555 0148
    </div>
    <div class="contact contact--web">WWW.DENTISTKALVO.COM</div>
    <div class="contact contact--address">2836 Thornbury Ln Rockville MD 20853</div>
  </section>

</div>
</body>
</html>
```